Journal to help kids Grades 1-5 be more creative thinkers

This is a journal for kids grades 1 - 5 where they can write, color, draw and be creative. It is designed to accompany our children's book and after-school program called Pebble Pathfinders Club. We want children to use their imagination and sense of wonder as they color, create new ideas, write stories and learn all about the creative problems solving method. We want them to learn about how to use their feelings and help others in their community. We have based this on our ORBIT method, which helps teachers teach their curriculum by engaging kids in relevant and meaningful ways and helping children of all ages learn how to think for themselves. We are a non-profit organization, so all the sales go to a scholarship fund that helps teachers pay for coaching and professional development. This journal may be used in after school programs, at home, or in classrooms. We wanted the inside to be black and white so kids feel free to make it their own but the cover should be bright and inviting. This is written and designed by Molly Drabek and Rosa Penhallow on behalf of Lantern 3 ORBIT.

Target Market(s)

Parents, schools, after school programs

Industry/Entity Type

Education

Other font styles liked:
• Fun for kids

Requirements
Must have
• Bright fun colors, our logo, easy to read font for kids
Nice to have
• Our 6 characters - but we do have them throughout book -

```html
<!DOCTYPE html>
<html lang="en">
<head>
<meta charset="utf-8">
<title>Pebble Pathfinders Journal – Cover</title>
<link rel="stylesheet" href="https://fonts.googleapis.com/css2?family=Fredoka:wght@600;700&family=Inter:wght@400;700&display=swap">
<style>
  :root {
    --backdrop: #272727;
    --paper: #ffffff;
    --orange: #f26a21;
    --blue: #41afc6;
    --green: #69a13e;
    --pink: #e94b86;
    --yellow: #fcd22a;
    --ink: #111111;
    --logo-ink: #3b3f7a;
  }
  * { box-sizing: border-box; margin: 0; padding: 0; }
  html, body { width: 1200px; height: 1200px; overflow: hidden; background: var(--backdrop); }

  .cover {
    position: absolute; left: 163px; top: 41px;
    width: 833px; height: 1077px;
    background: var(--paper);
    overflow: hidden;
    isolation: isolate;
  }

  /* Illustrated borders: pencils, leaves, clock, brush textures */
  .art { position: absolute; }
  .art-top {
    left: 0; top: 0; width: 100%; height: 300px;
    background: linear-gradient(90deg, var(--blue) 0%, var(--pink) 18%, #cfd6dc 35%, #fdd53a 48%, var(--blue) 62%, var(--green) 80%, #a2c13e 100%);
    -webkit-mask-image: linear-gradient(180deg, #000 35%, transparent 100%);
            mask-image: linear-gradient(180deg, #000 35%, transparent 100%);
    opacity: .85;
  }
  .art-left {
    left: 0; top: 220px; width: 170px; height: 460px;
    background: linear-gradient(180deg, var(--blue), #cfd6dc 45%, var(--yellow));
    -webkit-mask-image: radial-gradient(ellipse 100% 50% at 0% 50%, #000 35%, transparent 100%);
            mask-image: radial-gradient(ellipse 100% 50% at 0% 50%, #000 35%, transparent 100%);
    opacity: .8;
  }
  .art-right {
    right: 0; top: 110px; width: 260px; height: 400px;
    background: linear-gradient(200deg, var(--green), #a2c13e 50%, var(--orange));
    -webkit-mask-image: radial-gradient(ellipse 100% 50% at 100% 50%, #000 35%, transparent 100%);
            mask-image: radial-gradient(ellipse 100% 50% at 100% 50%, #000 35%, transparent 100%);
    opacity: .85;
  }
  .art-bottom {
    left: 0; bottom: 0; width: 100%; height: 330px;
    background: linear-gradient(90deg, var(--yellow) 0%, var(--pink) 22%, #cfd6dc 42%, #f4a640 60%, var(--blue) 80%, var(--green) 100%);
    -webkit-mask-image: linear-gradient(0deg, #000 30%, transparent 100%);
            mask-image: linear-gradient(0deg, #000 30%, transparent 100%);
    opacity: .85;
  }

  /* Title */
  .title-block { position: absolute; inset: 0; font-size: inherit; isolation: isolate; }
  .title {
    position: absolute; left: 0; width: 100%;
    font-family: "Fredoka", sans-serif; font-weight: 700;
    text-transform: uppercase; line-height: 1; white-space: nowrap;
  }
  .title span { position: relative; display: inline-block; }
  .title span::before {
    content: attr(data-text);
    position: absolute; left: 5px; top: 5px; z-index: -1;
    color: var(--paper);
    -webkit-text-stroke: 1.5px currentColor;
  }
  .title-line-1 { top: 380px; padding-left: 170px; font-size: 128px; color: var(--orange); }
  .title-line-2 { top: 520px; padding-left: 45px; font-size: 112px; color: var(--blue); letter-spacing: -1px; }
  .title-line-3 { top: 648px; padding-left: 258px; font-size: 104px; color: var(--green); }
  .title-line-1 span::before { -webkit-text-stroke-color: var(--orange); }
  .title-line-2 span::before { -webkit-text-stroke-color: var(--blue); }
  .title-line-3 span::before { -webkit-text-stroke-color: var(--green); }

  /* Club mark */
  .club-mark {
    position: absolute; left: 0; width: 100%; top: 870px;
    display: flex; justify-content: center; align-items: center; gap: 10px;
    font-family: "Fredoka", sans-serif; font-weight: 600; font-size: 22px;
    color: var(--logo-ink);
  }
  .club-mark .dot { width: 18px; height: 18px; border-radius: 50%; background: var(--logo-ink); }

  /* Credits */
  .byline {
    position: absolute; left: 0; width: 100%; top: 995px;
    text-align: center; padding-left: 20px;
    font-family: "Inter", sans-serif; font-size: 18px; color: var(--ink);
  }
  .byline strong { font-weight: 700; }
</style>
</head>
<body>
  <main class="cover">
    <div class="art art-top" role="img" aria-label="Colourful pencils, autumn leaves, an alarm clock and black brush-stroke textures along the top edge"></div>
    <div class="art art-left" role="img" aria-label="Blue pencil and yellow shape at the left edge"></div>
    <div class="art art-right" role="img" aria-label="Green pencil and orange swirl at the right edge"></div>
    <div class="art art-bottom" role="img" aria-label="Pink, grey and green pencils, a yellow leaf and dotted brush textures along the bottom edge"></div>

    <h1 class="title-block">
      <div class="title title-line-1"><span data-text="Pebble">Pebble</span></div>
      <div class="title title-line-2"><span data-text="Pathfinders">Pathfinders</span></div>
      <div class="title title-line-3"><span data-text="Journal">Journal</span></div>
    </h1>

    <div class="club-mark"><span class="dot"></span>Pebble Pathfinders Club</div>

    <p class="byline"><strong>written and designed by</strong> Molly Drabek and Rosa Penhallow</p>
  </main>
</body>
</html>
```